Cedarline Joinery eye catching business card

I need an eye catching business card that reflects my traditional, fun, handmade woodcraft shop. I make high end custom furniture and fine woodworking products, a lot of which are rustic, natural looking. We are a small shop but we produce awesome, one of a kind wood products, and our business card should reflect that. Our target audience is young professionals to retired folks who want a quality, local, handmade product. I'd like the Shop Nearby logo somewhere on the card, BUT not overwhelming, the main focus is my Logo, no preference on color whichever looks the best. Visit my website to get a feel for my company. Cedarlinejoinery.com
Target Market(s)
young professionals to retired folks. Any one who wants to furnish their home with quality handcrafted products.
Industry/Entity Type
Business
Contact Information for Business Card
Marlo Finch (555)417-6382
marlo@cedarlinejoinery.com
www.cedarlinejoinery.com
Look and feel

```html
<!DOCTYPE html>
<html lang="en">
<head>
<meta charset="utf-8">
<title>Cedarline Joinery – Business Card</title>
<link href="https://fonts.googleapis.com/css2?family=Oswald:wght@400;700&display=swap" rel="stylesheet">
<style>
  :root {
    --page: #ffffff;
    --wood-light: #b4773d;
    --wood-mid: #8e5526;
    --wood-dark: #6a3c1a;
    --seam: #4a2810;
    --brand-ink: #4d2a14;
    --tagline: #3e220f;
    --contact-ink: #fbf3e6;
    --photo-a: #5a3a22;
    --photo-b: #a96a3a;
    --photo-c: #8c2f2a;
    --badge: #e7b92a;
    --badge-ring: #5b7a1f;
  }
  html, body {
    margin: 0;
    padding: 0;
    width: 1195px;
    height: 1200px;
    overflow: hidden;
    background: var(--page);
  }
  .canvas {
    position: relative;
    width: 1195px;
    height: 1200px;
  }
  .card {
    position: absolute;
    top: 420px;
    width: 414px;
    height: 241px;
    overflow: hidden;
    font-family: "Oswald", sans-serif;
  }
  .card--front { left: 167px; }
  .card--back { left: 609px; }
  .wood {
    position: absolute;
    inset: 0;
    background: linear-gradient(100deg, var(--wood-mid) 0%, var(--wood-light) 45%, var(--wood-mid) 75%, var(--wood-dark) 100%);
  }
  .planks {
    position: absolute;
    inset: 0;
  }
  .brand {
    position: absolute;
    left: 0;
    right: 0;
    top: 52px;
    text-align: center;
    color: var(--brand-ink);
    font-weight: 700;
    text-transform: uppercase;
    line-height: 1;
  }
  .brand__main {
    display: block;
    font-size: 58px;
    letter-spacing: 5px;
  }
  .brand__sub {
    display: block;
    font-size: 24px;
    letter-spacing: 5px;
    margin-top: 8px;
  }
  .tagline {
    position: absolute;
    left: 0;
    right: 0;
    top: 188px;
    text-align: center;
    color: var(--tagline);
    font-size: 11px;
    font-weight: 400;
    letter-spacing: 2.5px;
    text-transform: uppercase;
  }
  .product-photo {
    position: absolute;
    left: 0;
    top: 0;
    width: 198px;
    height: 241px;
    background: linear-gradient(125deg, var(--photo-a) 0%, var(--photo-b) 40%, var(--photo-c) 60%, var(--photo-b) 75%, var(--photo-a) 100%);
    opacity: 0.92;
  }
  .contact {
    position: absolute;
    left: 198px;
    right: 0;
    top: 52px;
    text-align: center;
    color: var(--contact-ink);
    font-size: 12px;
    font-weight: 400;
    line-height: 28px;
  }
  .contact p { margin: 0; }
  .local-badge {
    position: absolute;
    left: 285px;
    top: 188px;
    width: 32px;
    height: 32px;
    border-radius: 50%;
    background: var(--badge);
    border: 3px solid var(--badge-ring);
    box-sizing: border-box;
  }
</style>
</head>
<body>
<main class="canvas">

  <section class="card card--front" aria-label="Business card front">
    <div class="wood" role="img" aria-label="Warm wood grain planks"></div>
    <svg class="planks" width="414" height="241" viewBox="0 0 414 241" aria-hidden="true">
      <g stroke="var(--seam)" stroke-width="2" opacity="0.55">
        <line x1="0" y1="30" x2="414" y2="30"/>
        <line x1="0" y1="78" x2="414" y2="78"/>
        <line x1="0" y1="126" x2="414" y2="126"/>
        <line x1="0" y1="174" x2="414" y2="174"/>
        <line x1="0" y1="216" x2="414" y2="216"/>
        <line x1="22" y1="0" x2="22" y2="241"/>
        <line x1="392" y1="0" x2="392" y2="241"/>
      </g>
    </svg>
    <h1 class="brand">
      <span class="brand__main">Cedarline</span>
      <span class="brand__sub">Joinery</span>
    </h1>
    <p class="tagline">Handmade in Harborvale, SC</p>
  </section>

  <section class="card card--back" aria-label="Business card back">
    <div class="wood" role="img" aria-label="Warm wood grain planks"></div>
    <svg class="planks" width="414" height="241" viewBox="0 0 414 241" aria-hidden="true">
      <g stroke="var(--seam)" stroke-width="2" opacity="0.55">
        <line x1="198" y1="22" x2="414" y2="22"/>
        <line x1="198" y1="78" x2="414" y2="78"/>
        <line x1="198" y1="136" x2="414" y2="136"/>
        <line x1="198" y1="186" x2="414" y2="186"/>
      </g>
    </svg>
    <div class="product-photo" role="img" aria-label="Photo of a striped handmade wooden cutting board"></div>
    <div class="contact">
      <p class="contact__name">Marlo Finch</p>
      <p class="contact__phone">Phone : (555)417-6382</p>
      <p class="contact__email">Email: marlo@cedarlinejoinery.com</p>
      <p class="contact__web">Visit us at cedarlinejoinery.com</p>
    </div>
    <div class="local-badge" role="img" aria-label="Shop Nearby badge"></div>
  </section>

</main>
</body>
</html>
```